Wedding and event Photography company.

We need a business card design for a photography company based in Singapore named LumaVek. Our core service offering is wedding photojournalism. We would like to see minimalistic designs that use the colour white. The final design should communicate a sense of ease and reliability.

The attached are a couple of visual reference which i found over the web, i hope it will helps.

Project Brief Update (14th July 2014):
- Please refrain from using any images from the website for the design. The laws and regulations over here does not allow me to distribute my client's images. Thanks!

Target Market(s)

Young and middle aged adults aged 24 - 38. With money to spend =D

Industry/Entity Type

Business

Contact Information for Business Card

Name: Dax Pell
Designation: Head Photographer
Mobile: +65 84126079
Email: tan@lumavek.example
Website: www.lumavek.example

Font styles to use
Other font styles liked:
• Baskerville URW

Colors

Designer to choose colors to be used in the design.

Requirements
Must have
• Must include:
• - The brand LumaVek
• - The logo attached
• - Please help to place the brand LumaVek with the logo according to your preferences.
• - Services
• - Wedding Photography
• - Portraiture
• - Photojournalism
Nice to have
• Looking forward to an elegant and simple design. Please see attached examples!
• Please use Serif Fonts
Should not have
• Please refrain from using dark tones for the majority of the design.
• Please refrain from letterpress and embossing.

```html
<!DOCTYPE html>
<html lang="en">
<head>
<meta charset="utf-8">
<title>LumaVek Business Card</title>
<link rel="stylesheet" href="https://fonts.googleapis.com/css2?family=Alegreya:wght@400&family=Bitter:wght@700&family=Open+Sans:wght@400&display=swap">
<style>
  :root {
    --stage: #4b4b4b;
    --card-light: #e8e8e8;
    --card-dark: #0b0b0b;
    --ink: #111111;
    --paper-text: #ffffff;
    --muted-text: #e2e2e2;
  }
  html, body {
    margin: 0;
    padding: 0;
    overflow: hidden;
  }
  .stage {
    position: relative;
    width: 1200px;
    height: 900px;
    background: var(--stage);
    overflow: hidden;
  }
  .card {
    position: absolute;
    top: 215px;
    width: 414px;
    height: 414px;
    border-radius: 50%;
    box-shadow: 0 3px 6px rgba(0, 0, 0, 0.35);
  }
  .card-front {
    left: 164px;
    background: var(--card-light);
  }
  .card-back {
    left: 623px;
    background: var(--card-dark);
    color: var(--paper-text);
    text-align: center;
  }
  .brand-dot {
    position: absolute;
    left: 189px;
    top: 140px;
    width: 36px;
    height: 36px;
    border-radius: 50%;
    background: var(--ink);
  }
  .brand-name {
    position: absolute;
    left: 0;
    right: 0;
    top: 228px;
    margin: 0;
    text-align: center;
    font-family: "Alegreya", Georgia, serif;
    font-weight: 400;
    font-size: 68px;
    line-height: 1;
    color: var(--ink);
  }
  .person-name {
    position: absolute;
    left: 0;
    right: 0;
    top: 94px;
    margin: 0;
    font-family: "Bitter", Georgia, serif;
    font-weight: 700;
    font-size: 24px;
    line-height: 1;
    letter-spacing: 0.5px;
  }
  .person-role {
    position: absolute;
    left: 0;
    right: 0;
    top: 129px;
    margin: 0;
    font-family: "Open Sans", Arial, sans-serif;
    font-size: 17px;
    line-height: 1;
    color: var(--muted-text);
  }
  .divider {
    position: absolute;
    left: 139px;
    top: 182px;
    width: 136px;
    height: 1px;
    background: var(--paper-text);
  }
  .contact-icons {
    position: absolute;
    left: 0;
    right: 0;
    top: 213px;
    display: flex;
    justify-content: center;
    gap: 7px;
  }
  .contact-icons svg {
    width: 17px;
    height: 17px;
  }
  .contact-list {
    position: absolute;
    left: 0;
    right: 0;
    top: 244px;
    margin: 0;
    padding: 0;
    list-style: none;
    font-family: "Open Sans", Arial, sans-serif;
    font-size: 17.5px;
    line-height: 24px;
  }
</style>
</head>
<body>
<main class="stage">
  <section class="card card-front" aria-label="Card front">
    <span class="brand-dot" aria-hidden="true"></span>
    <h1 class="brand-name">LumaVek</h1>
  </section>

  <section class="card card-back" aria-label="Card back">
    <h2 class="person-name">DAX PELL</h2>
    <p class="person-role">Head Photographer</p>
    <span class="divider" aria-hidden="true"></span>
    <div class="contact-icons" aria-hidden="true">
      <svg viewBox="0 0 16 16" class="icon-phone">
        <rect x="3.5" y="1" width="9" height="14" rx="1.5" fill="none" stroke="#fff" stroke-width="1.6"/>
        <rect x="5" y="3" width="6" height="8" fill="#fff"/>
        <circle cx="8" cy="13" r="0.9" fill="#fff"/>
      </svg>
      <svg viewBox="0 0 16 16" class="icon-mail">
        <rect x="1" y="3.5" width="14" height="9.5" fill="#fff"/>
        <path d="M1.5 4 L8 9 L14.5 4" fill="none" stroke="#0b0b0b" stroke-width="1.2"/>
        <path d="M1.5 12.5 L6 8 M14.5 12.5 L10 8" stroke="#0b0b0b" stroke-width="1"/>
      </svg>
      <svg viewBox="0 0 16 16" class="icon-web">
        <circle cx="8" cy="8" r="7" fill="#fff"/>
        <path d="M4 4.5 Q6 4 7 6 Q6 8 4.5 8.5 Q3.5 7 4 4.5Z M9 9 Q11 8.5 12 10 Q11 12.5 9.5 13 Q8.5 11 9 9Z M9.5 3 Q11.5 3.5 12.5 5.5 L10.5 5.5Z" fill="#0b0b0b"/>
      </svg>
    </div>
    <ul class="contact-list">
      <li>+65 84126079</li>
      <li>tan@lumavek.example</li>
      <li>www.lumavek.example</li>
    </ul>
  </section>
</main>
</body>
</html>
```